Letterhead to Prospective Clients

Create a letterhead (word & canva) that I will use to send letters to prospective clients and also include the Coralwood Estate Partners Logo, My Contact Details and Interchangeable "Suburb". Use the same font and colour pallete

Maris Dulworth | "Suburb" Specialist - Redlands & Surrounds
Mobile: 0417 862 095
Email: MD@CoralwoodEstatePartners.com.au

```html
<!DOCTYPE html>
<html lang="en">
<head>
<meta charset="utf-8">
<title>Coralwood Estate Partners – Letterhead</title>
<link rel="stylesheet" href="https://fonts.googleapis.com/css2?family=Jost:wght@300;400;500&family=Josefin+Sans:wght@300;400&display=swap">
<style>
  :root {
    --navy: #0b1640;
    --gold: #d4a674;
    --ink: #3a3a3f;
    --paper: #ffffff;
    --desk: #e8e8ea;
    --white: #ffffff;
  }
  * { margin: 0; padding: 0; box-sizing: border-box; }
  html, body { width: 1200px; height: 703px; overflow: hidden; background: var(--desk); }
  .canvas { position: relative; width: 1200px; height: 703px; }
  .letterhead {
    position: absolute; left: 360px; top: 12px;
    width: 481px; height: 680px;
    background: var(--paper);
    box-shadow: 0 4px 18px rgba(0,0,0,.12);
    overflow: hidden;
    font-family: "Jost", "Futura", sans-serif;
  }
  .header-band, .footer-band { position: absolute; left: 0; width: 481px; }
  .header-band { top: 0; height: 210px; }
  .footer-band { bottom: 0; height: 110px; }

  .brand {
    position: absolute; left: 30px; top: 72px; width: 150px;
    font-family: "Josefin Sans", sans-serif; font-weight: 300;
    color: var(--white); text-align: center;
  }
  .brand-name { font-size: 19px; line-height: 1; letter-spacing: .1em; white-space: nowrap; }
  .brand-sub { font-size: 6px; letter-spacing: .3em; margin-top: 7px; color: var(--gold); white-space: nowrap; }

  .divider { position: absolute; left: 192px; top: 58px; width: 1px; height: 58px; background: var(--gold); }

  .agent { position: absolute; left: 204px; top: 52px; color: var(--white); white-space: nowrap; }
  .agent-name { font-family: "Josefin Sans", sans-serif; font-size: 13.5px; font-weight: 400; color: var(--gold); letter-spacing: .04em; }
  .agent-role { font-size: 6.6px; letter-spacing: .06em; margin-top: 1px; text-transform: uppercase; }
  .contact-list { list-style: none; margin-top: 9px; font-size: 6.2px; letter-spacing: .06em; }
  .contact-list li { display: flex; align-items: center; gap: 5px; height: 10px; }
  .contact-list svg { width: 6px; height: 6px; flex: none; }

  .agent-photo {
    position: absolute; left: 390px; top: 14px; width: 58px; height: 108px;
    background: linear-gradient(180deg, #2d3a5c 0%, #3c4a6d 55%, #1e2945 100%);
    border-radius: 29px 29px 2px 2px;
  }

  .letter-body {
    position: absolute; left: 40px; top: 222px; width: 405px;
    font-size: 6.3px; line-height: 2.25; color: var(--ink); letter-spacing: .02em;
  }
  .letter-body p { margin-bottom: 10px; }
  .salutation { margin-bottom: 12px; }
  .closing { margin-top: 22px; }
  .signature {
    margin-top: 14px; width: 100px; height: 34px;
    background: linear-gradient(90deg, #e7e7ea, #f3f3f5);
    border-radius: 3px;
  }

  .service-areas {
    position: absolute; right: 40px; bottom: 38px;
    text-align: center; font-size: 7px; letter-spacing: .08em;
    color: var(--navy); line-height: 1.6; text-transform: uppercase;
  }
</style>
</head>
<body>
<div class="canvas">
  <article class="letterhead">
    <svg class="header-band" viewBox="0 0 481 210" aria-hidden="true">
      <path d="M0 0 H481 V132 C440 118 380 112 310 138 C230 170 130 205 45 192 C25 189 10 184 0 178 Z" fill="var(--navy)"/>
    </svg>

    <div class="brand">
      <div class="brand-name">CORALWOOD</div>
      <div class="brand-sub">ESTATE PARTNERS</div>
    </div>

    <div class="divider"></div>

    <div class="agent">
      <div class="agent-name">MARIS DULWORTH</div>
      <div class="agent-role">Specialist - Redlands &amp; Surrounds</div>
      <ul class="contact-list">
        <li><svg viewBox="0 0 10 10"><rect x="2.5" y=".5" width="5" height="9" rx="1" fill="none" stroke="var(--gold)" stroke-width="1.2"/></svg>0417 862 095</li>
        <li><svg viewBox="0 0 10 10"><rect x=".5" y="2" width="9" height="6" fill="var(--gold)"/><path d="M.5 2 L5 5.5 L9.5 2" fill="none" stroke="var(--navy)" stroke-width=".8"/></svg>MD@CORALWOODESTATEPARTNERS.COM.AU</li>
        <li><svg viewBox="0 0 10 10"><circle cx="5" cy="5" r="4.3" fill="none" stroke="var(--gold)" stroke-width="1.2"/><path d="M1 5 H9 M5 1 V9" stroke="var(--gold)" stroke-width=".8"/></svg>CORALWOODESTATEPARTNERS.COM.AU</li>
      </ul>
    </div>

    <div class="agent-photo" role="img" aria-label="Portrait photo of Maris Dulworth"></div>

    <section class="letter-body">
      <p class="salutation">Dear Sir,</p>
      <p>Lorem ipsum dolor sit amet, consectetur adipiscing elit. Aenean ut ipsum eget massa hendrerit vestibulum vel in velit. Donec pretium neque velit. Aliquam porta lectus nec mauris ornare venenatis. Vivamus non est turpis, et cursus sem. Mauris vehicula erat in diam auctor at bibendum nisl lacinia.</p>
      <p>Morbi imperdiet neque vehicula nunc convallis gravida. Vestibulum iaculis pretium placerat. Integer consequat, est sit amet facilisis eleifend, nibh nibh varius orci, eget dapibus arcu dui non purus. Pellentesque in magna mauris. Duis enim sapien, dictum vitae condimentum a, pulvinar vel lacus. Mauris et molestie nibh. Vestibulum vitae nulla at metus elementum porta sit amet interdum elit. Nulla sollicitudin neque eu nulla volutpat congue.</p>
      <p>Etiam pellentesque, velit id dapibus fermentum, turpis sapien ornare dui, ac tincidunt ligula odio congue purus. Nunc sed ante dui, in porta lectus. Cras nec sem lorem. In hac habitasse platea dictumst. Maecenas id diam quis dui porta tristique. Sed id egestas felis. Donec ullamcorper mattis posuere. Phasellus fermentum eleifend tortor vel dapibus. Vestibulum ante ipsum.</p>
      <p class="closing">Sincerely,</p>
      <div class="signature" role="img" aria-label="Handwritten signature of Maris Dulworth"></div>
    </section>

    <svg class="footer-band" viewBox="0 0 481 110" aria-hidden="true">
      <path d="M0 70 C60 115 150 110 250 70 C330 38 400 20 481 40 V110 H0 Z" fill="var(--gold)"/>
    </svg>
    <div class="service-areas">Alexandra Hills | Capalaba<br>Sheldon &amp; Mt Cotton</div>
  </article>
</div>
</body>
</html>
```